Creative Businesss Card desgin!

Create a business card for our business Glint window cleaning!
We are open to creative ideas as long as it maintains a professional image.

Target Market(s)

Small Commercial window cleaning clients including car dealerships, strata manager, cafe

Industry/Entity Type

Window Cleaning

Contact Information for Business Card

Darren Pilkey
General Manager
Glint Window Cleaning

darren@glintservices.com.au
pane-tidy-corner.com.au
Ph: 1800 GO GLINT
Mob: 0438 572 619

Colors
fbed22
0392cd

Requirements
Should not have
• Stock window cleaning/ squeegee graphics

```html
<!DOCTYPE html>
<html lang="en">
<head>
<meta charset="utf-8">
<title>Glint Window Cleaning – Business Card</title>
<link rel="stylesheet" href="https://fonts.googleapis.com/css2?family=Archivo:wght@800&family=Raleway:wght@400;700&display=swap">
<style>
  :root {
    --page-bg: #1a1a1a;
    --card-navy: #2c5d8c;
    --card-navy-deep: #22496f;
    --band-blue: #2f68ad;
    --accent-blue: #0392cd;
    --chevron-fill: #2a4d7c;
    --brand-yellow: #fbed22;
    --strip-yellow: #d9d46a;
    --icon-dark: #2b2b2b;
    --text-white: #ffffff;
  }
  * { margin: 0; padding: 0; box-sizing: border-box; }
  html, body {
    width: 1200px;
    height: 1200px;
    overflow: hidden;
    background: var(--page-bg);
  }
  .canvas {
    position: relative;
    width: 1200px;
    height: 1200px;
    display: flex;
    align-items: center;
    justify-content: center;
  }
  .business-card {
    position: relative;
    width: 1000px;
    height: 580px;
    border-radius: 38px;
    overflow: hidden;
    background: var(--card-navy);
  }
  .skyline-photo {
    position: absolute;
    inset: 0;
    background:
      linear-gradient(180deg, rgba(70,120,170,0.55) 0%, rgba(44,93,140,0) 45%),
      linear-gradient(90deg, var(--card-navy-deep) 0%, var(--card-navy) 40%, #336596 70%, var(--card-navy-deep) 100%);
  }
  .card-shapes {
    position: absolute;
    inset: 0;
    width: 100%;
    height: 100%;
  }
  .contact-person,
  .contact-details {
    position: absolute;
    top: 34px;
    font-family: "Raleway", Helvetica, sans-serif;
    color: var(--text-white);
    font-size: 18px;
    line-height: 26px;
    letter-spacing: 0.5px;
  }
  .contact-person { left: 56px; }
  .contact-details { right: 56px; text-align: right; }
  .contact-person .person-name {
    display: block;
    font-weight: 700;
    font-size: 22px;
    line-height: 30px;
  }
  .contact-person .person-title { display: block; font-weight: 400; }
  .contact-details span { display: block; font-weight: 400; }
  .contact-details .label { display: inline; font-weight: 700; }
  .brand-name {
    position: absolute;
    top: 160px;
    left: 0;
    right: 0;
    text-align: center;
    font-family: "Archivo", Arial, sans-serif;
    font-weight: 800;
    color: var(--brand-yellow);
    text-transform: uppercase;
    line-height: 1;
  }
  .brand-name .brand-main {
    display: block;
    font-size: 112px;
    letter-spacing: 4px;
  }
  .brand-name .brand-sub {
    display: block;
    margin-top: 10px;
    font-size: 40px;
    letter-spacing: 2px;
  }
  .social-link {
    position: absolute;
    top: 382px;
    width: 300px;
    text-align: center;
    font-family: "Raleway", Helvetica, sans-serif;
    color: var(--text-white);
  }
  .social-link.is-left { left: 140px; }
  .social-link.is-right { left: 460px; }
  .social-dot {
    display: block;
    width: 58px;
    height: 58px;
    margin: 0 auto 12px;
    border-radius: 50%;
    background: var(--icon-dark);
  }
  .social-site {
    display: block;
    font-weight: 700;
    font-size: 25px;
    letter-spacing: 1px;
  }
  .social-handle {
    display: block;
    font-weight: 400;
    font-size: 23px;
    letter-spacing: 1px;
    margin-top: 2px;
  }
</style>
</head>
<body>
<main class="canvas">
  <article class="business-card">
    <div class="skyline-photo" role="img" aria-label="Blue-tinted photograph of a city skyline with tall office towers"></div>

    <svg class="card-shapes" viewBox="0 0 1000 580" aria-hidden="true">
      <polygon class="contact-band" points="0,470 250,470 300,405 690,405 800,580 0,580" fill="var(--band-blue)"/>
      <polygon class="corner-strip" points="0,540 200,540 170,580 0,580" fill="var(--strip-yellow)"/>
      <polygon class="corner-strip" points="790,565 1000,540 1000,580 800,580" fill="var(--strip-yellow)"/>
      <polygon class="chevron-left" points="-10,150 125,285 -10,420" fill="var(--chevron-fill)" stroke="var(--accent-blue)" stroke-width="22" stroke-linejoin="miter"/>
      <polygon class="chevron-right" points="1010,210 880,340 1010,470" fill="var(--chevron-fill)" stroke="var(--accent-blue)" stroke-width="22" stroke-linejoin="miter"/>
    </svg>

    <div class="contact-person">
      <span class="person-name">Darren Pilkey</span>
      <span class="person-title">General Manager</span>
      <span class="person-title">Glint Window Cleaning</span>
    </div>

    <div class="contact-details">
      <span><span class="label">Ph:</span> 1800 GO GLINT</span>
      <span><span class="label">Mob:</span> 0438 572 619</span>
      <span>darren@glintservices.com.au</span>
      <span>pane-tidy-corner.com.au</span>
    </div>

    <h1 class="brand-name">
      <span class="brand-main">Glint</span>
      <span class="brand-sub">Window Cleaning</span>
    </h1>

    <div class="social-link is-left">
      <span class="social-dot"></span>
      <span class="social-site">chirpline.com</span>
      <span class="social-handle">glintwindowcleaning</span>
    </div>

    <div class="social-link is-right">
      <span class="social-dot"></span>
      <span class="social-site">friendboard.com</span>
      <span class="social-handle">glintwindowcleaning</span>
    </div>
  </article>
</main>
</body>
</html>
```